Falcon Letterhead

Looking for a design template for our company’s official letterheads & business cards.It has to be mainly white and include our company logo, website, social media handle, address, phone number. Visit our website to have an idea of our brand identity and colours. Please use the same font that we are using in our website.
Target Market(s)
Lubricants & Greases, Industrial markets, Automotive
Font styles to use
Other font styles liked:
- Saira Extra-Condensed
Colors
ffffff
000000
fbee3f
Requirements
Must have
- It must be consistent with our brand identity. It must use the same exact yellow (Pantone color: 102C) and black (Pantone color: K100) as our brand colors.
- Must also use our font attached (Saira.zip). It's called Saira Extra-Condensed.
- We intend to use the FALCON logo and not the small mini-FN logo.
- On the design we must include ALL of the following:
- E-mail: info@falconoils.example
- @FalconGreases
- www.falconoils.example
- Address: P.O. Boc 4728, Qurain 53004, Kuwait
- Phone: (+965) 24718395
- Gulf Marwa Oils logo (attached). The logo attached is in Blue/Red but you can select one solid color for all of it such as BLACK or YELLOW depending on what background color you'll select.
Nice to have
- Like it to be as professional and as modern as possible. It has look clean, slick and classy.
Should not have
- Too many different colors.

```html
<!DOCTYPE html>
<html lang="en">
<head>
<meta charset="utf-8">
<title>Falcon Stationery</title>
<link href="https://fonts.googleapis.com/css2?family=Saira+Extra+Condensed:wght@600;700&family=Mulish:wght@300;400;600;700&display=swap" rel="stylesheet">
<style>
  :root {
    --brand-yellow: #fbee3f;
    --brand-black: #000000;
    --paper: #ffffff;
    --backdrop: #efefef;
    --ink: #3a3a3a;
    --ink-soft: #8a8a8a;
    --rule: #e4e4e4;
  }
  * { box-sizing: border-box; margin: 0; padding: 0; }
  html, body { width: 1200px; height: 800px; overflow: hidden; }
  body {
    background: var(--backdrop);
    font-family: "Mulish", Arial, sans-serif;
    color: var(--ink);
    position: relative;
  }

  /* Wordmark */
  .wordmark { display: flex; align-items: center; gap: 8px; }
  .wordmark__square { background: var(--brand-yellow); flex: none; }
  .wordmark__name {
    font-family: "Saira Extra Condensed", "Arial Narrow", sans-serif;
    font-weight: 700;
    color: var(--brand-black);
    letter-spacing: 1px;
    line-height: 1;
  }

  .partner { display: flex; align-items: center; gap: 6px; }
  .partner__dot { border-radius: 50%; background: var(--brand-black); flex: none; }
  .partner__name { font-weight: 700; color: var(--brand-black); text-transform: uppercase; letter-spacing: .5px; }

  .contact-list { list-style: none; }
  .contact-list li { display: flex; align-items: center; gap: 5px; }
  .contact-list .bullet { width: 5px; height: 5px; background: var(--brand-yellow); flex: none; }

  .divider { width: 2px; background: var(--brand-yellow); align-self: stretch; }

  /* Letterhead */
  .letterhead {
    position: absolute; left: 640px; top: 30px;
    width: 524px; height: 740px;
    background: var(--paper);
    box-shadow: 0 2px 10px rgba(0,0,0,.08);
    padding: 50px 48px 0;
  }
  .letterhead__header { display: flex; align-items: center; gap: 18px; height: 70px; }
  .letterhead__header .wordmark__square { width: 22px; height: 22px; }
  .letterhead__header .wordmark__name { font-size: 46px; }
  .letterhead__contacts { font-size: 8px; line-height: 1.6; color: var(--ink); }
  .letterhead__body { margin-top: 48px; }
  .salutation { font-size: 13px; color: var(--ink); margin-bottom: 16px; }
  .letterhead__body p { font-size: 8.5px; line-height: 1.75; color: var(--ink-soft); margin-bottom: 12px; }
  .sign-off { margin-top: 22px; font-size: 10px; }
  .sign-off__name { font-weight: 700; color: var(--brand-black); margin-top: 4px; }
  .sign-off__role { color: var(--ink-soft); font-size: 8.5px; }
  .signature { width: 90px; height: 16px; margin-top: 8px; background: linear-gradient(90deg, #d6d6d6, #ececec); border-radius: 8px; }
  .letterhead__footer {
    position: absolute; left: 48px; right: 48px; bottom: 40px;
    display: flex; justify-content: flex-end;
  }
  .letterhead__footer .partner__dot { width: 14px; height: 14px; }
  .letterhead__footer .partner__name { font-size: 10px; }
  .letterhead__edge { position: absolute; left: 0; right: 0; bottom: 0; }
  .letterhead__edge .edge-line { height: 2px; background: var(--brand-black); }
  .letterhead__edge .edge-band { height: 10px; background: var(--brand-yellow); }

  /* Business cards */
  .card {
    position: absolute; left: 90px;
    width: 480px; height: 274px;
    background: var(--paper);
    box-shadow: 0 2px 10px rgba(0,0,0,.08);
  }
  .card--front { top: 100px; display: flex; align-items: center; padding: 0 40px; gap: 24px; }
  .card--front .wordmark__square { width: 20px; height: 20px; }
  .card--front .wordmark__name { font-size: 48px; }
  .card__details { font-size: 10px; line-height: 1.6; }
  .card__name { font-weight: 700; color: var(--brand-yellow); font-size: 13px; text-transform: uppercase; letter-spacing: 1px; }
  .card__role { color: var(--ink-soft); margin-bottom: 6px; }
  .card--back { top: 420px; display: flex; flex-direction: column; align-items: center; justify-content: center; gap: 16px; }
  .card--back .wordmark__square { width: 24px; height: 24px; }
  .card--back .wordmark__name { font-size: 60px; }
  .card--back .partner__dot { width: 12px; height: 12px; }
  .card--back .partner__name { font-size: 10px; }
</style>
</head>
<body>

<section class="card card--front" aria-label="Business card front">
  <div class="wordmark">
    <span class="wordmark__square"></span>
    <span class="wordmark__name">FALCON</span>
  </div>
  <span class="divider"></span>
  <div class="card__details">
    <div class="card__name">Rashid Kamal</div>
    <div class="card__role">Director</div>
    <ul class="contact-list">
      <li><span class="bullet"></span>P.O. Boc 4728, Qurain 53004, Kuwait</li>
      <li><span class="bullet"></span>(+965) 24718395</li>
      <li><span class="bullet"></span>info@falconoils.example</li>
      <li><span class="bullet"></span>www.falconoils.example</li>
      <li><span class="bullet"></span>@FalconGreases</li>
    </ul>
  </div>
</section>

<section class="card card--back" aria-label="Business card back">
  <div class="wordmark">
    <span class="wordmark__square"></span>
    <span class="wordmark__name">FALCON</span>
  </div>
  <div class="partner">
    <span class="partner__dot"></span>
    <span class="partner__name">Gulf Marwa Oils Co.</span>
  </div>
</section>

<section class="letterhead" aria-label="Letterhead">
  <header class="letterhead__header">
    <div class="wordmark">
      <span class="wordmark__square"></span>
      <span class="wordmark__name">FALCON</span>
    </div>
    <span class="divider"></span>
    <ul class="contact-list letterhead__contacts">
      <li>P.O. Boc 4728,</li>
      <li>Qurain 53004, Kuwait</li>
      <li><span class="bullet"></span>(+965) 24718395</li>
      <li><span class="bullet"></span>info@falconoils.example</li>
      <li><span class="bullet"></span>www.falconoils.example</li>
      <li><span class="bullet"></span>@FalconGreases</li>
    </ul>
  </header>

  <main class="letterhead__body">
    <p class="salutation">Dear sir/Madam,</p>
    <p>Lorem ipsum dolor sit amet, an vel recteque dissentiet, detracto albucius platonem ex vel, eros repudiandae cu. Atqui aliquando nec an, unum graece adolescens vel ad. Id odio scae has, ludico euismod atomorum ius ea, cum ea honestatis quaerendum theophrastus. Mea</p>
    <p>Lorem ipsum dolor sit amet, an vel recteque dissentiet, detracto albucius platonem ex vel, eros repudiandae cu. Atqui aliquando nec an, unum graece adolescens vel ad. Id odio scae has, ludico euismod atomorum ius ea, cum ea honestatis quaerendum theophrastus. Quo etiam pertinax ex, te dolore repudiandae cu. Atqui aliquando nec an, unum graece adolescens. Mea</p>
    <p>Lorem ipsum dolor sit amet, an vel recteque dissentiet, detracto albucius platonem ex vel, eros repudiandae cu. Atqui aliquando nec an, unum graece adolescens vel ad. Id odio scae has, ludico euismod atomorum ius ea, cum ea honestatis quaerendum theophrastus. Mea</p>
    <p>Lorem ipsum dolor sit amet, an vel recteque dissentiet, detracto albucius platonem ex vel, eros repudiandae cu. Atqui aliquando nec an, unum graece adolescens vel ad. Id odio scae has, cum ea honestatis quaerendum theophrastus. Mea</p>
    <div class="sign-off">
      <div>Kind regards,</div>
      <div class="sign-off__name">Daniel Whitmore</div>
      <div class="sign-off__role">Chemist</div>
      <div class="signature" role="img" aria-label="Handwritten signature"></div>
    </div>
  </main>

  <footer class="letterhead__footer">
    <div class="partner">
      <span class="partner__dot"></span>
      <span class="partner__name">Gulf Marwa Oils Co.</span>
    </div>
  </footer>

  <div class="letterhead__edge">
    <div class="edge-line"></div>
    <div class="edge-band"></div>
  </div>
</section>

</body>
</html>
```